We need a nice stationary and business card design for our new mobile ultrasound company.
Kestral Sonics, LLC
We need a nice stationary and business card design for our new mobile ultrasound company.  - Medical
Creative Brief
Bright & Fun-filled
Tomaso Fairbank
Vice President
5817 E. Halvering Ct
Tomaso.Fairbank@kestralsonics.example
KestralSonics.example
Please do not add our address to your design.

```html
<!DOCTYPE html>
<html lang="en">
<head>
<meta charset="utf-8">
<title>Kestral Sonics, LLC — Stationery Set</title>
<link rel="stylesheet" href="https://fonts.googleapis.com/css2?family=Cinzel:wght@600&family=Lato:wght@400&display=swap">
<style>
  :root {
    --page: #ffffff;
    --paper: #ffffff;
    --edge: #d9d9d9;
    --brand-blue: #1d5c9b;
    --brand-light: #6fa3d4;
    --ink: #6b6b6b;
    --rule: #b9b9b9;
    --ghost: #eeeeee;
  }
  * { box-sizing: border-box; margin: 0; padding: 0; }
  html, body { width: 1200px; height: 681px; overflow: hidden; background: var(--page); }
  .board { position: relative; width: 1200px; height: 681px; }
  .board-frame { position: absolute; left: 14px; top: 16px; width: 1168px; height: 630px; border: 1px solid var(--edge); }
  .sheet { position: absolute; background: var(--paper); border: 1px solid var(--edge); overflow: hidden; }

  .brand { position: absolute; display: flex; align-items: center; gap: 6px; }
  .brand-dot { border-radius: 50%; background: var(--brand-light); flex: none; }
  .brand-name { font-family: "Cinzel", serif; font-weight: 600; color: var(--brand-blue); line-height: 1.05; white-space: nowrap; }

  .divider { position: absolute; width: 1px; background: var(--rule); }
  .contact { position: absolute; font-family: "Lato", sans-serif; color: var(--ink); line-height: 1.35; white-space: nowrap; }

  .envelope-front { left: 48px; top: 72px; width: 492px; height: 192px; }
  .envelope-back { left: 48px; top: 300px; width: 456px; height: 204px; }
  .envelope-flap { position: absolute; inset: 0; }
  .letterhead { left: 619px; top: 43px; width: 336px; height: 586px; }
  .card-front { left: 965px; top: 216px; width: 120px; height: 84px; }
  .card-back { left: 965px; top: 317px; width: 120px; height: 86px; }
  .ghost-circle { position: absolute; border-radius: 50%; background: var(--ghost); }
</style>
</head>
<body>
<main class="board">
  <div class="board-frame"></div>

  <section class="sheet envelope-front" aria-label="Envelope front">
    <div class="brand" style="left:14px; top:20px;">
      <span class="brand-dot" style="width:22px; height:22px;"></span>
      <span class="brand-name" style="font-size:15px;">Kestral<br>Sonics</span>
    </div>
    <div class="divider" style="left:132px; top:16px; height:38px;"></div>
    <div class="contact" style="left:140px; top:17px; font-size:7px;">
      Phone: (555) 014-2290<br>
      Fax: (555) 014-2291<br>
      Tomaso.Fairbank@kestralsonics.example<br>
      KestralSonics.example
    </div>
  </section>

  <section class="sheet envelope-back" aria-label="Envelope back">
    <svg class="envelope-flap" viewBox="0 0 456 204" preserveAspectRatio="none" aria-hidden="true">
      <polyline points="0,10 28,66 428,66 456,10" fill="none" stroke="#9a9a9a" stroke-width="1.2"/>
    </svg>
    <div class="brand" style="left:50%; top:20px; transform:translateX(-50%); flex-direction:column; gap:4px;">
      <span class="brand-dot" style="width:20px; height:20px;"></span>
      <span class="brand-name" style="font-size:9px;">Kestral Sonics</span>
    </div>
  </section>

  <section class="sheet letterhead" aria-label="Letterhead">
    <div class="brand" style="left:20px; top:20px;">
      <span class="brand-dot" style="width:24px; height:24px;"></span>
      <span class="brand-name" style="font-size:16px;">Kestral<br>Sonics</span>
    </div>
    <div class="divider" style="left:142px; top:14px; height:44px;"></div>
    <div class="contact" style="left:150px; top:14px; font-size:7.5px;">
      Phone: (555) 014-2290<br>
      Fax: (555) 014-2291<br>
      Tomaso.Fairbank@kestralsonics.example<br>
      KestralSonics.example
    </div>
    <span class="ghost-circle" style="left:216px; top:404px; width:104px; height:104px;"></span>
  </section>

  <section class="sheet card-front" aria-label="Business card front">
    <div class="brand" style="left:6px; top:20px; gap:4px;">
      <span class="brand-dot" style="width:12px; height:12px;"></span>
      <span class="brand-name" style="font-size:7.5px;">Kestral<br>Sonics</span>
    </div>
    <div class="contact" style="left:56px; top:14px; font-size:3.2px;">
      Tomaso Fairbank<br>
      Vice President<br>
      Phone: (555) 014-2290<br>
      Tomaso.Fairbank@kestralsonics.example<br>
      KestralSonics.example
    </div>
  </section>

  <section class="sheet card-back" aria-label="Business card back">
    <div class="brand" style="left:50%; top:22px; transform:translateX(-50%); flex-direction:column; gap:3px;">
      <span class="brand-dot" style="width:22px; height:22px;"></span>
      <span class="brand-name" style="font-size:6px;">Kestral Sonics</span>
    </div>
  </section>
</main>
</body>
</html>
```